Willowmere Family Program (special education services) needs a Brochure Design

We need a brochure design for a new company. We are an Willowmere Family Program providing special education, speech, occupational and physical therapy to children birth - 3 years of age. The children we provide services for have a wide range of disabilities. Please include some stock photos if possible. Brochure text is attached.
Updates

Project Deadline Extended Reason: 1. We would like to see pictures that are multicultural (not all Caucasian).2. Some of the pictures (which were taken from our website) that were used by designers are of children that are older than 3 yrs. Please use new/different pictures of children birth-3 yrs. 3. Update the text that is in the brochure. Original line is: "The Willowmere Family Program (WFP) is a statewide public program for infants and toddlers with special needs". Replace with "The Willowmere Family Program (WFP) is a statewide public program for infants and toddlers, ages birth to 3 years, with special needs". Added Monday, February 6, 2017

Target Market(s)

Parents, Doctors, Daycare Providers

Industry/Entity Type

Education

Font styles to use
Serif
Sans Serif

Requirements
Must have
• A balance between professional looking, while child friendly and colorful
Nice to have
• A few stock pictures of children (birth-age 3)

```html
<!DOCTYPE html>
<html lang="en">
<head>
<meta charset="utf-8">
<title>Willowmere Family Program – Brochure Cover</title>
<link href="https://fonts.googleapis.com/css2?family=Cinzel:wght@500;700&family=Open+Sans:wght@400;600&display=swap" rel="stylesheet">
<style>
  :root {
    --page-bg: #e9e6e1;
    --paper: #f3f1ec;
    --purple: #7a2c93;
    --purple-deep: #5a1f78;
    --purple-light: #9a4fb3;
    --ink: #2b2b2b;
    --white: #ffffff;
  }
  * { margin: 0; padding: 0; box-sizing: border-box; }
  html, body { width: 1200px; height: 817px; overflow: hidden; }
  body {
    background: var(--page-bg);
    display: flex;
    align-items: center;
    justify-content: center;
  }
  .cover {
    position: relative;
    width: 370px;
    height: 785px;
    background: var(--paper);
    overflow: hidden;
    box-shadow: 0 8px 24px rgba(0,0,0,0.18);
  }
  .cover-photo {
    position: absolute;
    inset: 0 0 auto 0;
    height: 310px;
    background: radial-gradient(circle at 55% 45%, #6fc247 0%, #d9306b 28%, #f2c43a 40%, #3a86c8 52%, #8a6f75 68%, #4a3d40 100%);
  }
  .cover-body {
    position: absolute;
    left: 0; right: 0; top: 280px; bottom: 0;
    background: var(--paper);
    border-top-left-radius: 34px;
  }
  .org-lockup {
    position: absolute;
    left: 44px; top: 40px;
    display: flex;
    align-items: center;
    gap: 14px;
  }
  .org-mark {
    width: 34px; height: 34px;
    border-radius: 50%;
    background: var(--purple);
    flex: none;
  }
  .org-name {
    font-family: "Cinzel", serif;
    font-weight: 500;
    font-size: 15px;
    line-height: 1.2;
    color: var(--ink);
    border-left: 1px solid var(--ink);
    padding-left: 12px;
  }
  .headline {
    position: absolute;
    left: 0; right: 0; top: 108px;
    text-align: center;
    font-family: "Cinzel", serif;
    font-weight: 700;
    font-size: 29px;
    line-height: 1.1;
    color: var(--purple);
    letter-spacing: 0.5px;
  }
  .footer-band {
    position: absolute;
    left: 0; right: 0; bottom: 0;
    height: 190px;
  }
  .footer-band svg { display: block; width: 100%; height: 100%; }
  .footer-info {
    position: absolute;
    left: 0; right: 0; bottom: 56px;
    text-align: center;
    color: var(--white);
    font-family: "Open Sans", sans-serif;
  }
  .footer-url { font-size: 14px; font-weight: 600; letter-spacing: 0.3px; }
  .footer-social {
    margin-top: 8px;
    display: flex; justify-content: center; gap: 10px;
  }
  .footer-social span {
    width: 12px; height: 12px; border-radius: 50%;
    background: var(--white);
  }
</style>
</head>
<body>
  <article class="cover">
    <div class="cover-photo" role="img" aria-label="Photo of a smiling toddler holding up a hand covered in bright rainbow paint"></div>
    <section class="cover-body">
      <div class="org-lockup">
        <span class="org-mark"></span>
        <span class="org-name">Bright Sprouts<br>Development Center</span>
      </div>
      <h1 class="headline">Welcome to<br>the Willowmere<br>Family<br>Program</h1>
    </section>
    <footer class="footer-band">
      <svg viewBox="0 0 370 190" preserveAspectRatio="none" aria-hidden="true">
        <defs>
          <linearGradient id="bandGrad" x1="0" y1="0" x2="1" y2="1">
            <stop offset="0" stop-color="#9a4fb3"/>
            <stop offset="1" stop-color="#5a1f78"/>
          </linearGradient>
        </defs>
        <path d="M0 30 C30 10 45 50 75 30 S120 10 150 28 S200 50 230 28 S280 5 310 22 S350 40 370 20 L370 190 L0 190 Z" fill="url(#bandGrad)"/>
        <path d="M0 42 C30 22 45 62 75 42 S120 22 150 40 S200 62 230 40 S280 17 310 34 S350 52 370 32" fill="none" stroke="#ffffff" stroke-width="3"/>
      </svg>
      <div class="footer-info">
        <div class="footer-url">www.brightsproutskids.org</div>
        <div class="footer-social"><span></span><span></span><span></span></div>
      </div>
    </footer>
  </article>
</body>
</html>
```